Build PowerPoint for New Logo & Letterhead

I have started my own consulting firm and created a logo and letterhead (attached) am looking PowerPoint template. My name is Dorian Pekkarinen and the company is called Q Harbor Consulting. We primarily use PowerPoint files to display analyses, maps and key talking points from interviews and/or recommendations. We use the documents more to facilitate discussion with our target audiences. Most of the time our PowerPoint document is printed as handouts for our clients and not projected.

Target Market(s)

Healthcare provider organizations (hospitals, health systems, physician groups)

Industry/Entity Type

Healthcare

Font styles to use
Sans Serif

Colors
abd036
1f9ad1
0355a3

Requirements
Must have
• I would like to cover page to play off of the letterhead in some fashion. I want the design to provide plenty of space for text, graphics, maps, pictures, etc.
• We will usually include our clients logo somewhere on the document. Historically it is prominent on the cover page and then in one of the corners on all of the pages thereafter.

```html
<!DOCTYPE html>
<html lang="en">
<head>
<meta charset="utf-8">
<title>Q Harbor Consulting – Presentation Template</title>
<link href="https://fonts.googleapis.com/css2?family=Open+Sans:wght@400;600;700&family=Ubuntu:wght@500;700&display=swap" rel="stylesheet">
<style>
:root{
  --green:#abd036;
  --blue:#1f9ad1;
  --navy:#0355a3;
  --ink:#222;
  --text:#5a5a5a;
  --grey:#bfbfbf;
  --canvas:#ececec;
}
*{box-sizing:border-box;margin:0;padding:0}
html,body{width:905px;height:1200px;overflow:hidden;background:var(--canvas)}
body{position:relative;font-family:"Open Sans",Arial,sans-serif;color:var(--text)}
.slide{position:absolute;width:286px;height:161px;background:#fff;overflow:hidden;box-shadow:0 1px 2px rgba(0,0,0,.12)}
.c1{left:15px}.c2{left:310px}.c3{left:606px}
.r1{top:18px}.r2{top:186px}.r3{top:354px}.r4{top:522px}.r5{top:690px}.r6{top:858px}.r7{top:1026px}
.title{position:absolute;left:15px;top:13px;font-family:"Ubuntu",Arial,sans-serif;font-weight:500;font-size:11px;color:#333}
.pg{position:absolute;right:6px;top:2px;width:7px;height:7px;background:var(--blue);color:#fff;font-size:3px;text-align:center;line-height:7px}
.rule{position:absolute;left:22px;right:0;bottom:10px;height:1.2px;background:var(--blue)}
.rule::after{content:"";position:absolute;right:0;top:0;width:38%;height:2px;background:var(--navy)}
.mark{position:absolute;left:20px;bottom:5px;font-size:4px;font-weight:700;color:var(--navy)}
.mark::before{content:"";display:inline-block;width:4px;height:4px;background:var(--blue);margin-right:2px;vertical-align:-0.5px}
.copy{position:absolute;left:0;right:0;bottom:3px;text-align:center;font-size:2.4px;color:#999}
.client{position:absolute;right:7px;bottom:3px;font-size:4px;font-weight:700;color:var(--ink)}
.head{font-size:5px;font-weight:600;color:var(--blue);margin-bottom:2px}
.txt{font-size:3.8px;line-height:1.4;color:var(--text)}
.txt ul{list-style:none}
.txt li{padding-left:4px;position:relative;margin-bottom:1.5px}
.txt li::before{content:"•";position:absolute;left:0}
.txt li.sub{padding-left:9px}
.txt li.sub::before{content:"–";left:5px}
.abs{position:absolute}
.photo{position:absolute;background:linear-gradient(135deg,#dfe8ef,#b9cad8)}
.band{position:absolute;left:0;width:100%;height:40px}
.logo-name{font-weight:700;color:var(--navy)}
</style>
</head>
<body>

<!-- Row 1 -->
<section class="slide c1 r1" style="background:linear-gradient(135deg,#3aa7dc,#1f8fd0 55%,#1a7cc4)">
  <div class="photo" role="img" aria-label="Faint photo of healthcare professionals walking, tinted blue" style="inset:0;background:linear-gradient(180deg,rgba(255,255,255,.08),rgba(3,85,163,.18))"></div>
  <p class="abs" style="left:0;right:0;top:57px;text-align:center;color:#fff;font-size:5.2px;line-height:1.35"><b>Lorem ipsum</b> dolor sit amet, consectetur adipiscing<br>elit. Suspendisse eget ligula mollis, mattis libero eget, rutrum ipsum.</p>
  <p class="abs" style="left:0;right:0;top:80px;text-align:center;color:#e6f3fb;font-size:3px">Copyright © 2016 Q Harbor Consulting All rights reserved.</p>
  <p class="abs logo-name" style="left:0;right:0;top:108px;text-align:center;color:#fff;font-size:6px;letter-spacing:.5px">Q HARBOR CONSULTING</p>
</section>

<section class="slide c2 r1">
  <svg class="abs" style="left:0;top:0" width="286" height="161">
    <polyline points="0,108 158,108 178,123 286,123" fill="none" stroke="var(--green)" stroke-width="1"/>
    <polyline points="0,111 156,111 176,126 286,126" fill="none" stroke="var(--blue)" stroke-width="2"/>
    <polyline points="0,114 154,114 174,129 286,129" fill="none" stroke="var(--navy)" stroke-width="1"/>
  </svg>
  <h1 class="abs" style="left:8px;top:124px;font-family:Ubuntu,sans-serif;font-size:11px;font-weight:700;color:#222">Presentation Title</h1>
  <p class="abs" style="left:8px;top:138px;font-size:5px;color:#333">Subheading Presentation Title</p>
  <p class="abs" style="left:8px;top:150px;font-size:3.5px;color:#333">May 2016</p>
  <p class="abs logo-name" style="right:10px;top:145px;font-size:5px">Q Harbor Consulting</p>
</section>

<section class="slide c3 r1">
  <h1 class="abs" style="left:16px;top:47px;font-family:Ubuntu,sans-serif;font-size:14px;font-weight:700;color:#222">Presentation Title</h1>
  <p class="abs" style="left:16px;top:64px;font-size:6px;color:#333">Subheading Presentation Title</p>
  <p class="abs" style="left:16px;top:79px;font-size:4px;color:#333">May 2016</p>
  <p class="abs logo-name" style="left:16px;top:133px;font-size:5px">Q Harbor</p>
  <p class="abs" style="left:52px;top:128px;font-size:3.5px;color:var(--blue);line-height:3">Email: dorian@qharborconsulting.co<br>Telephone: 555.010.2231</p>
  <svg class="abs" style="left:0;top:0" width="286" height="161">
    <polyline points="0,125 286,125" stroke="var(--blue)" stroke-width="1"/>
    <polyline points="45,150 225,150 235,155 286,155" fill="none" stroke="var(--blue)" stroke-width="1"/>
    <polyline points="0,147 100,147" stroke="var(--green)" stroke-width="1"/>
    <polyline points="225,152 286,152" stroke="var(--navy)" stroke-width="2"/>
  </svg>
  <span class="client" style="bottom:10px">client logo here</span>
</section>

<!-- Row 2 -->
<section class="slide c1 r2">
  <svg class="abs" style="left:0;top:0" width="286" height="161">
    <polyline points="0,122 158,122 178,137 286,137" fill="none" stroke="var(--green)" stroke-width="1"/>
    <polyline points="0,125 156,125 176,140 286,140" fill="none" stroke="var(--blue)" stroke-width="2"/>
    <polyline points="0,158 286,158" stroke="var(--navy)" stroke-width="2"/>
  </svg>
  <h2 class="abs" style="left:7px;top:139px;font-family:Ubuntu,sans-serif;font-size:8px;font-weight:700;color:#222">Section Slide</h2>
  <p class="abs" style="left:7px;top:150px;font-size:5px;color:#333">Divider Presentation Title</p>
</section>

<section class="slide c2 r2">
  <span class="pg">4</span>
  <h2 class="title">Table of Content</h2>
  <div class="abs txt" style="left:18px;top:37px;width:260px;display:grid;grid-template-columns:repeat(3,1fr);row-gap:8px;column-gap:8px">
    <div><p style="display:flex;align-items:center;gap:3px;font-weight:600;color:#333"><svg width="12" height="12"><circle cx="6" cy="6" r="5.3" fill="#fff" stroke="var(--green)"/><text x="6" y="8" font-size="5" text-anchor="middle" fill="var(--navy)">1</text></svg>Lorem Ipsum</p><p>Lorem ipsum dolor sit amet, te ullum corpora delicata duo. Rebum insolens pri eu. No alia tota modus qui.</p></div>
    <div><p style="display:flex;align-items:center;gap:3px;font-weight:600;color:#333"><svg width="12" height="12"><circle cx="6" cy="6" r="5.3" fill="#fff" stroke="var(--green)"/><text x="6" y="8" font-size="5" text-anchor="middle" fill="var(--navy)">2</text></svg>Lorem Ipsum</p><p>Lorem ipsum dolor sit amet, te ullum corpora delicata duo. Rebum insolens pri eu. No alia tota modus qui.</p></div>
    <div><p style="display:flex;align-items:center;gap:3px;font-weight:600;color:#333"><svg width="12" height="12"><circle cx="6" cy="6" r="5.3" fill="#fff" stroke="var(--green)"/><text x="6" y="8" font-size="5" text-anchor="middle" fill="var(--navy)">3</text></svg>Lorem Ipsum</p><p>Lorem ipsum dolor sit amet, te ullum corpora delicata duo. Rebum insolens pri eu. No alia tota modus qui.</p></div>
    <div><p style="display:flex;align-items:center;gap:3px;font-weight:600;color:#333"><svg width="12" height="12"><circle cx="6" cy="6" r="5.3" fill="#fff" stroke="var(--green)"/><text x="6" y="8" font-size="5" text-anchor="middle" fill="var(--navy)">4</text></svg>Lorem Ipsum</p><p>Lorem ipsum dolor sit amet, te ullum corpora delicata duo. Rebum insolens pri eu. No alia tota modus qui.</p></div>
    <div><p style="display:flex;align-items:center;gap:3px;font-weight:600;color:#333"><svg width="12" height="12"><circle cx="6" cy="6" r="5.3" fill="#fff" stroke="var(--green)"/><text x="6" y="8" font-size="5" text-anchor="middle" fill="var(--navy)">5</text></svg>Lorem Ipsum</p><p>Lorem ipsum dolor sit amet, te ullum corpora delicata duo. Rebum insolens pri eu. No alia tota modus qui.</p></div>
    <div><p style="display:flex;align-items:center;gap:3px;font-weight:600;color:#333"><svg width="12" height="12"><circle cx="6" cy="6" r="5.3" fill="#fff" stroke="var(--green)"/><text x="6" y="8" font-size="5" text-anchor="middle" fill="var(--navy)">6</text></svg>Lorem Ipsum</p><p>Lorem ipsum dolor sit amet, te ullum corpora delicata duo. Rebum insolens pri eu. No alia tota modus qui.</p></div>
  </div>
  <div class="rule"></div><span class="mark">Q</span><span class="copy">Copyright © 2016 Q Harbor Consulting. All rights reserved.</span><span class="client">client logo here</span>
</section>

<section class="slide c3 r2">
  <span class="pg">5</span>
  <h2 class="title">One Column</h2>
  <div class="abs txt" style="left:15px;top:36px;width:250px">
    <p class="head">Lorem Ipsum</p>
    <ul>
      <li>Lorem ipsum dolor sit amet, te ullum corpora delicata duo. Rebum insolens pri eu. No alia tota modus qui.</li>
      <li class="sub">Sint brute at usu. Duo iisque apparaet adversarium at.</li>
      <li>Lorem ipsum dolor sit amet, te ullum corpora delicata duo. Rebum insolens pri eu. No alia tota modus qui.</li>
      <li class="sub">Sint brute at usu. Duo iisque apparaet adversarium at.</li>
      <li>Lorem ipsum dolor sit amet, te ullum corpora delicata duo. Rebum insolens pri eu. No alia tota modus qui.</li>
      <li class="sub">Sint brute at usu. Duo iisque apparaet adversarium at.</li>
      <li>Lorem ipsum dolor sit amet, te ullum corpora delicata duo. Rebum insolens pri eu. No alia tota modus qui.</li>
      <li class="sub">Sint brute at usu. Duo iisque apparaet adversarium at.</li>
    </ul>
  </div>
  <div class="rule"></div><span class="mark">Q</span><span class="copy">Copyright © 2016 Q Harbor Consulting. All rights reserved.</span><span class="client">client logo here</span>
</section>

<!-- Row 3 -->
<section class="slide c1 r3">
  <span class="pg">6</span>
  <h2 class="title">Two Column</h2>
  <div class="abs txt" style="left:17px;top:37px;width:130px">
    <p class="head">Lorem Ipsum</p>
    <ul><li>Lorem ipsum dolor sit amet, te ullum corpora delicata duo. Rebum insolens pri eu. No alia tota modus qui.</li><li class="sub">Sint brute at usu. Duo iisque apparaet adversarium at.</li><li>Lorem ipsum dolor sit amet, te ullum corpora delicata duo. Rebum insolens pri eu. No alia tota modus qui.</li><li class="sub">Sint brute at usu. Duo iisque apparaet adversarium at.</li><li>Lorem ipsum dolor sit amet, te ullum corpora delicata duo. Rebum insolens pri eu. No alia tota modus qui.</li></ul>
  </div>
  <div class="abs txt" style="left:148px;top:37px;width:125px">
    <p class="head">Lorem Ipsum</p>
    <ul><li>Lorem ipsum dolor sit amet, te ullum corpora delicata duo. Rebum insolens pri eu. No alia tota modus qui.</li><li class="sub">Sint brute at usu. Duo iisque apparaet adversarium at.</li><li>Lorem ipsum dolor sit amet, te ullum corpora delicata duo. Rebum insolens pri eu. No alia tota modus qui.</li><li class="sub">Sint brute at usu. Duo iisque apparaet adversarium at.</li><li>Lorem ipsum dolor sit amet, te ullum corpora delicata duo. Rebum insolens pri eu. No alia tota modus qui.</li></ul>
  </div>
  <div class="rule"></div><span class="mark">Q</span><span class="copy">Copyright © 2016 Q Harbor Consulting. All rights reserved.</span><span class="client">client logo here</span>
</section>

<section class="slide c2 r3">
  <span class="pg">7</span>
  <h2 class="title">Left Column</h2>
  <div class="abs txt" style="left:17px;top:37px;width:125px">
    <p class="head">Lorem Ipsum</p>
    <ul><li>Lorem ipsum dolor sit amet, te ullum corpora delicata duo. Rebum insolens pri eu. No alia tota modus qui.</li><li class="sub">Sint brute at usu. Duo iisque apparaet adversarium at.</li><li>Lorem ipsum dolor sit amet, te ullum corpora delicata duo. Rebum insolens pri eu. No alia tota modus qui.</li><li class="sub">Sint brute at usu. Duo iisque apparaet adversarium at.</li><li>Lorem ipsum dolor sit amet, te ullum corpora delicata duo. Rebum insolens pri eu. No alia tota modus qui.</li></ul>
  </div>
  <svg class="abs" style="left:150px;top:38px" width="120" height="100" viewBox="0 0 120 100">
    <polygon points="60,2 70,21 50,21" fill="#dcdcdc"/>
    <polygon points="48,24 72,24 83,45 37,45" fill="var(--navy)"/>
    <polygon points="35,48 85,48 96,69 24,69" fill="var(--blue)"/>
    <polygon points="22,72 98,72 110,94 10,94" fill="var(--green)"/>
  </svg>
  <div class="rule"></div><span class="mark">Q</span><span class="copy">Copyright © 2016 Q Harbor Consulting. All rights reserved.</span><span class="client">client logo here</span>
</section>

<section class="slide c3 r3">
  <span class="pg">8</span>
  <div class="photo" role="img" aria-label="Photo of a smiling doctor in a white coat with a stethoscope" style="left:0;top:0;width:138px;height:147px;background:linear-gradient(160deg,#eef3f7,#c9d7e3 60%,#a9bccd)"></div>
  <h2 class="title" style="left:148px;font-size:9.5px">Right Column With Image</h2>
  <div class="abs txt" style="left:150px;top:38px;width:125px">
    <p class="head" style="color:var(--green)">Lorem Ipsum</p>
    <ul><li>Lorem ipsum dolor sit amet, te ullum corpora delicata duo. Rebum insolens pri eu. No alia tota modus qui.</li><li class="sub">Sint brute at usu. Duo iisque apparaet adversarium at.</li><li>Lorem ipsum dolor sit amet, te ullum corpora delicata duo. Rebum insolens pri eu. No alia tota modus qui.</li><li class="sub">Sint brute at usu. Duo iisque apparaet adversarium at.</li><li>Lorem ipsum dolor sit amet, te ullum corpora delicata duo. Rebum insolens pri eu. No alia tota modus qui.</li></ul>
  </div>
  <div class="rule"></div><span class="mark">Q</span><span class="copy">Copyright © 2016 Q Harbor Consulting. All rights reserved.</span><span class="client">client logo here</span>
</section>

<!-- Row 4 -->
<section class="slide c1 r4">
  <span class="pg">9</span>
  <h2 class="title">Our Team</h2>
  <div class="abs" style="left:30px;top:35px;width:230px;display:grid;grid-template-columns:repeat(3,1fr);row-gap:6px;text-align:center">
    <div><div class="photo" role="img" aria-label="Team member portrait" style="position:relative;margin:0 auto;width:36px;height:36px;border-radius:50%;border:1.5px solid var(--green)"></div><p style="font-size:4.2px;color:var(--navy);font-style:italic;font-weight:600">John Doe</p><p style="font-size:3.2px">Doctor</p></div>
    <div><div class="photo" role="img" aria-label="Team member portrait" style="position:relative;margin:0 auto;width:36px;height:36px;border-radius:50%;border:1.5px solid var(--green)"></div><p style="font-size:4.2px;color:var(--navy);font-style:italic;font-weight:600">John Doe</p><p style="font-size:3.2px">Doctor</p></div>
    <div><div class="photo" role="img" aria-label="Team member portrait" style="position:relative;margin:0 auto;width:36px;height:36px;border-radius:50%;border:1.5px solid var(--green)"></div><p style="font-size:4.2px;color:var(--navy);font-style:italic;font-weight:600">John Doe</p><p style="font-size:3.2px">Doctor</p></div>
    <div><div class="photo" role="img" aria-label="Team member portrait" style="position:relative;margin:0 auto;width:36px;height:36px;border-radius:50%;border:1.5px solid var(--green)"></div><p style="font-size:4.2px;color:var(--navy);font-style:italic;font-weight:600">John Doe</p><p style="font-size:3.2px">Doctor</p></div>
    <div><div class="photo" role="img" aria-label="Team member portrait" style="position:relative;margin:0 auto;width:36px;height:36px;border-radius:50%;border:1.5px solid var(--green)"></div><p style="font-size:4.2px;color:var(--navy);font-style:italic;font-weight:600">John Doe</p><p style="font-size:3.2px">Doctor</p></div>
    <div><div class="photo" role="img" aria-label="Team member portrait" style="position:relative;margin:0 auto;width:36px;height:36px;border-radius:50%;border:1.5px solid var(--green)"></div><p style="font-size:4.2px;color:var(--navy);font-style:italic;font-weight:600">John Doe</p><p style="font-size:3.2px">Doctor</p></div>
  </div>
  <div class="rule"></div><span class="mark">Q</span><span class="copy">Copyright © 2016 Q Harbor Consulting. All rights reserved.</span><span class="client">client logo here</span>
</section>

<section class="slide c2 r4">
  <span class="pg">10</span>
  <h2 class="title">Table Sample</h2>
  <svg class="abs" style="left:15px;top:36px" width="257" height="104" viewBox="0 0 257 104">
    <rect x="0" y="0" width="64" height="11" fill="var(--green)"/>
    <rect x="64" y="0" width="64" height="11" fill="var(--blue)"/>
    <rect x="128" y="0" width="65" height="11" fill="var(--navy)"/>
    <rect x="193" y="0" width="64" height="11" fill="#9e9e9e"/>
    <g font-size="4" fill="#fff" font-weight="600" text-anchor="middle" font-family="Open Sans,sans-serif">
      <text x="32" y="7.5">Lorem ipsum</text><text x="96" y="7.5">Lorem ipsum 1</text><text x="160" y="7.5">Lorem ipsum 2</text><text x="225" y="7.5">Lorem ipsum 3</text>
    </g>
    <rect x="0" y="11" width="257" height="30" fill="#e6e6e6"/>
    <rect x="0" y="41" width="257" height="30" fill="#fff"/>
    <rect x="0" y="71" width="257" height="15" fill="#e6e6e6"/>
    <rect x="0" y="86" width="257" height="18" fill="#fff"/>
    <g fill="#888">
      <rect x="4" y="15" width="52" height="1.5"/><rect x="68" y="15" width="52" height="1.5"/><rect x="132" y="15" width="52" height="1.5"/><rect x="197" y="15" width="52" height="1.5"/>
      <rect x="4" y="19" width="44" height="1.5"/><rect x="68" y="19" width="40" height="1.5"/><rect x="132" y="19" width="46" height="1.5"/><rect x="197" y="19" width="44" height="1.5"/>
      <rect x="4" y="45" width="52" height="1.5"/><rect x="68" y="45" width="52" height="1.5"/><rect x="132" y="45" width="52" height="1.5"/><rect x="197" y="45" width="52" height="1.5"/>
      <rect x="4" y="49" width="40" height="1.5"/><rect x="68" y="49" width="44" height="1.5"/><rect x="132" y="49" width="40" height="1.5"/><rect x="197" y="49" width="38" height="1.5"/>
      <rect x="4" y="75" width="52" height="1.5"/><rect x="68" y="75" width="52" height="1.5"/><rect x="132" y="75" width="52" height="1.5"/><rect x="197" y="75" width="52" height="1.5"/>
      <rect x="4" y="90" width="52" height="1.5"/><rect x="68" y="90" width="52" height="1.5"/><rect x="132" y="90" width="52" height="1.5"/><rect x="197" y="90" width="52" height="1.5"/>
    </g>
  </svg>
  <div class="rule"></div><span class="mark">Q</span><span class="copy">Copyright © 2016 Q Harbor Consulting. All rights reserved.</span><span class="client">client logo here</span>
</section>

<section class="slide c3 r4">
  <span class="pg">11</span>
  <h2 class="title">About Us</h2>
  <div class="photo" role="img" aria-label="Portrait photo of a smiling doctor" style="left:14px;top:40px;width:100px;height:100px;background:linear-gradient(160deg,#f2f5f8,#cbd8e3)"></div>
  <div class="abs txt" style="left:128px;top:42px;width:148px">
    <p class="head" style="font-weight:400">Lorem Ipsum is simply dummy</p>
    <p>Text of the printing and typesetting industry. Lorem Ipsum has been the industry's standard dummy text ever since the 1500s, when an unknown printer took a galley of type and scrambled it to make a type specimen book. It has survived not only five centuries, but also the leap into electronic typesetting, remaining essentially unchanged. It was popularised in the 1960s with the release of Letraset sheets containing Lorem Ipsum passages, and more recently with desktop publishing software.</p>
    <p style="margin-top:1px">Lorem Ipsum has been the industry's standard dummy text ever since the 1500s, when an unknown printer took a galley of type and scrambled.</p>
  </div>
  <div class="rule"></div><span class="mark">Q</span><span class="copy">Copyright © 2016 Q Harbor Consulting. All rights reserved.</span><span class="client">client logo here</span>
</section>

<!-- Row 5 -->
<section class="slide c1 r5">
  <span class="pg">12</span>
  <h2 class="title">Pie Chart Sample</h2>
  <p class="abs" style="left:0;right:0;top:41px;text-align:center;font-size:7px;font-weight:600;color:#444">Lorem ipsum dolar sit amet</p>
  <svg class="abs" style="left:100px;top:52px" width="90" height="90" viewBox="0 0 90 90">
    <g transform="rotate(-90 45 45)">
      <circle cx="45" cy="45" r="20" fill="none" stroke="var(--green)" stroke-width="40" stroke-dasharray="72.88 125.66"/>
      <circle cx="45" cy="45" r="20" fill="none" stroke="var(--blue)" stroke-width="40" stroke-dasharray="28.9 125.66" stroke-dashoffset="-72.88"/>
      <circle cx="45" cy="45" r="20" fill="none" stroke="var(--navy)" stroke-width="40" stroke-dasharray="12.57 125.66" stroke-dashoffset="-101.78"/>
      <circle cx="45" cy="45" r="20" fill="none" stroke="#e2e2e2" stroke-width="40" stroke-dasharray="11.31 125.66" stroke-dashoffset="-114.35"/>
    </g>
    <g font-size="4.5" fill="#fff" font-family="Open Sans,sans-serif" text-anchor="middle">
      <text x="66" y="53">58%</text><text x="26" y="61">23%</text><text x="29" y="34">10%</text><text x="41" y="20" fill="#888">5%</text>
    </g>
  </svg>
  <p class="abs" style="left:0;right:0;top:147px;text-align:center;font-size:3px;color:#777;word-spacing:6px">● Lorem ipsum ● Lorem ipsum ● Lorem ipsum ● Lorem ipsum</p>
  <div class="rule" style="bottom:10px"></div><span class="mark">Q</span><span class="client">client logo here</span>
</section>

<section class="slide c2 r5">
  <span class="pg">13</span>
  <h2 class="title">Basic Chevron Process</h2>
  <svg class="abs" style="left:20px;top:37px" width="250" height="30" viewBox="0 0 250 30">
    <polygon points="0,0 80,0 92,15 80,30 0,30" fill="var(--green)"/>
    <polygon points="84,0 166,0 178,15 166,30 84,30 96,15" fill="var(--blue)"/>
    <polygon points="170,0 238,0 250,15 238,30 170,30 182,15" fill="var(--navy)"/>
    <g font-size="6" fill="#fff" font-family="Open Sans,sans-serif" text-anchor="middle"><text x="44" y="17">Lorem ipsum</text><text x="134" y="17">Lorem ipsum</text><text x="216" y="17">Lorem ipsum</text></g>
  </svg>
  <div class="abs txt" style="left:25px;top:75px;width:245px;display:grid;grid-template-columns:repeat(3,1fr);column-gap:12px">
    <ul><li>Lorem ipsum dolor sit amet, consectetur adipiscing elit.</li><li>Nunc quis dui dolor.</li><li>Maecenas sem nibh, congue a urna non, volutpat porttitor justo.</li></ul>
    <ul><li>Lorem ipsum dolor sit amet, consectetur adipiscing elit.</li><li>Nunc quis dui dolor.</li><li>Maecenas sem nibh, congue a urna non, volutpat porttitor justo.</li></ul>
    <ul><li>Lorem ipsum dolor sit amet, consectetur adipiscing elit.</li><li>Nunc quis dui dolor.</li><li>Maecenas sem nibh, congue a urna non, volutpat porttitor justo.</li></ul>
  </div>
  <div class="rule"></div><span class="mark">Q</span><span class="copy">Copyright © 2016 Q Harbor Consulting. All rights reserved.</span><span class="client">client logo here</span>
</section>

<section class="slide c3 r5">
  <span class="pg">14</span>
  <h2 class="title">Linier VEEN</h2>
  <svg class="abs" style="left:30px;top:45px" width="230" height="90" viewBox="0 0 230 90">
    <circle cx="50" cy="45" r="40" fill="var(--green)" opacity=".85"/>
    <circle cx="115" cy="45" r="40" fill="var(--blue)" opacity=".85"/>
    <circle cx="180" cy="45" r="40" fill="var(--navy)" opacity=".85"/>
  </svg>
  <div class="abs" style="left:45px;top:72px;width:200px;display:grid;grid-template-columns:repeat(3,1fr);column-gap:25px;text-align:center;font-size:3.6px;line-height:1.35;color:#fff">
    <p>Lorem ipsum dolor sit amet, consectetur adipiscing elit. Nunc quis dui dolor. Maecenas sem nibh, congue a urna non, volutpat porttitor justo.</p>
    <p>Lorem ipsum dolor sit amet, consectetur adipiscing elit. Nunc quis dui dolor. Maecenas sem nibh, congue a urna non, volutpat porttitor justo.</p>
    <p>Lorem ipsum dolor sit amet, consectetur adipiscing elit. Nunc quis dui dolor. Maecenas sem nibh, congue a urna non, volutpat porttitor justo.</p>
  </div>
  <div class="rule"></div><span class="mark">Q</span><span class="copy">Copyright © 2016 Q Harbor Consulting. All rights reserved.</span><span class="client">client logo here</span>
</section>

<!-- Row 6 -->
<section class="slide c1 r6">
  <span class="pg">15</span>
  <h2 class="title">Bar Chart Sample</h2>
  <p class="abs" style="left:0;right:0;top:28px;text-align:center;font-size:6px;font-weight:600;color:#444">Lorem ipsum dolor sit amet</p>
  <svg class="abs" style="left:15px;top:38px" width="260" height="105" viewBox="0 0 260 105">
    <g stroke="#eee" stroke-width=".5"><line x1="18" y1="10" x2="255" y2="10"/><line x1="18" y1="26" x2="255" y2="26"/><line x1="18" y1="42" x2="255" y2="42"/><line x1="18" y1="58" x2="255" y2="58"/><line x1="18" y1="74" x2="255" y2="74"/></g>
    <line x1="18" y1="90" x2="255" y2="90" stroke="#aaa" stroke-width=".5"/>
    <g font-size="3.5" fill="#888" font-family="Open Sans,sans-serif"><text x="12" y="91">0</text><text x="12" y="75">1</text><text x="12" y="59">2</text><text x="12" y="43">3</text><text x="12" y="27">4</text><text x="12" y="11">5</text></g>
    <rect x="28" y="33" width="9" height="57" fill="var(--green)"/>
    <rect x="52" y="59" width="9" height="31" fill="var(--green)"/>
    <rect x="76" y="45" width="9" height="45" fill="var(--green)"/>
    <rect x="100" y="31" width="9" height="59" fill="var(--blue)"/>
    <rect x="124" y="61" width="9" height="29" fill="var(--blue)"/>
    <rect x="148" y="71" width="9" height="19" fill="var(--blue)"/>
    <rect x="172" y="14" width="9" height="76" fill="var(--navy)"/>
    <rect x="196" y="51" width="9" height="39" fill="var(--navy)"/>
    <rect x="220" y="65" width="9" height="25" fill="var(--navy)"/>
    <rect x="244" y="37" width="9" height="53" fill="#9e9e9e"/>
    <g font-size="3" fill="#888" font-family="Open Sans,sans-serif" text-anchor="middle"><text x="32" y="97">Category 1</text><text x="56" y="97">Category 2</text><text x="80" y="97">Category 3</text><text x="104" y="97">Category 4</text><text x="128" y="97">Category 5</text><text x="152" y="97">Category 6</text><text x="176" y="97">Category 7</text><text x="200" y="97">Category 8</text><text x="224" y="97">Category 9</text><text x="248" y="97">Category 10</text></g>
  </svg>
  <div class="rule"></div><span class="mark">Q</span><span class="client">client logo here</span>
</section>

<section class="slide c2 r6">
  <span class="pg">16</span>
  <h2 class="title">Line Chart Sample</h2>
  <svg class="abs" style="left:15px;top:30px" width="260" height="115" viewBox="0 0 260 115">
    <g stroke="#eee" stroke-width=".5"><line x1="15" y1="8" x2="250" y2="8"/><line x1="15" y1="22" x2="250" y2="22"/><line x1="15" y1="36" x2="250" y2="36"/><line x1="15" y1="50" x2="250" y2="50"/><line x1="15" y1="64" x2="250" y2="64"/><line x1="15" y1="78" x2="250" y2="78"/></g>
    <line x1="15" y1="92" x2="250" y2="92" stroke="#aaa" stroke-width=".5"/>
    <g font-size="3.5" fill="#888" font-family="Open Sans,sans-serif"><text x="9" y="93">0</text><text x="9" y="79">1</text><text x="9" y="65">2</text><text x="9" y="51">3</text><text x="9" y="37">4</text><text x="9" y="23">5</text><text x="9" y="9">6</text></g>
    <polyline points="35,36 98,64 162,57 226,22" fill="none" stroke="var(--green)" stroke-width="1.2"/>
    <polyline points="35,64 98,36 162,71 226,50" fill="none" stroke="var(--navy)" stroke-width="1.2"/>
    <polyline points="35,57 98,71 162,50 226,29" fill="none" stroke="var(--blue)" stroke-width="1.2"/>
    <g fill="var(--green)"><rect x="33.5" y="34.5" width="3" height="3"/><rect x="96.5" y="62.5" width="3" height="3"/><rect x="160.5" y="55.5" width="3" height="3"/><rect x="224.5" y="20.5" width="3" height="3"/></g>
    <g fill="var(--navy)"><rect x="33.5" y="62.5" width="3" height="3"/><rect x="96.5" y="34.5" width="3" height="3"/><rect x="160.5" y="69.5" width="3" height="3"/><rect x="224.5" y="48.5" width="3" height="3"/></g>
    <g fill="var(--blue)"><rect x="33.5" y="55.5" width="3" height="3"/><rect x="96.5" y="69.5" width="3" height="3"/><rect x="160.5" y="48.5" width="3" height="3"/><rect x="224.5" y="27.5" width="3" height="3"/></g>
    <g font-size="3.5" fill="#888" font-family="Open Sans,sans-serif" text-anchor="middle"><text x="35" y="99">Jan</text><text x="98" y="99">Feb</text><text x="162" y="99">Mar</text><text x="226" y="99">Apr</text></g>
    <g font-size="3" fill="#888" font-family="Open Sans,sans-serif" text-anchor="middle"><text x="90" y="108">— Lorem ipsum 1</text><text x="130" y="108">— Lorem ipsum 2</text><text x="170" y="108">— Lorem ipsum 3</text></g>
  </svg>
  <div class="rule"></div><span class="mark">Q</span><span class="client">client logo here</span>
</section>

<section class="slide c3 r6">
  <span class="pg">17</span>
  <h2 class="title">Graphic Sample</h2>
  <svg class="abs" style="left:98px;top:40px" width="90" height="100" viewBox="0 0 90 100">
    <circle cx="45" cy="50" r="31" fill="none" stroke="#c8c8c8" stroke-width=".6"/>
    <g fill="#fff" stroke="var(--green)" stroke-width="1.3">
      <circle cx="45" cy="19" r="7"/><circle cx="72" cy="34" r="7"/><circle cx="72" cy="66" r="7"/>
      <circle cx="45" cy="81" r="7"/><circle cx="18" cy="66" r="7"/><circle cx="18" cy="34" r="7"/>
    </g>
    <g fill="none" stroke="var(--navy)" stroke-width=".8">
      <circle cx="44" cy="18" r="2.2"/><line x1="45.6" y1="19.6" x2="48" y2="22"/>
      <path d="M72 30 v4 M70 34 h4 M69.5 36 a2.5 2.5 0 0 0 5 0"/>
      <path d="M70 63.5 h4 v4 h-4z M72 67.5 v2"/>
      <rect x="43" y="77" width="4" height="7.5" rx=".6"/>
      <circle cx="18" cy="66" r="3"/><circle cx="18" cy="66" r="1"/>
      <rect x="14.5" y="31" width="7" height="5"/><line x1="18" y1="36" x2="18" y2="38"/>
    </g>
    <text x="45" y="53" font-size="6" font-weight="700" fill="var(--navy)" text-anchor="middle" font-family="Open Sans,sans-serif">Q Harbor</text>
  </svg>
  <div class="txt" style="position:absolute;left:0;right:0;font-size:3.6px">
    <p class="abs" style="left:105px;top:47px;width:78px;text-align:center">Lorem ipsum dolor sit amet, consectetur adipiscing elit</p>
    <p class="abs" style="left:105px;top:-12px;width:78px;text-align:center;transform:translateY(0)"></p>
  </div>
  <p class="abs txt" style="left:104px;top:33px;width:80px;text-align:center;font-size:3.6px">Lorem ipsum dolor sit amet, consectetur adipiscing elit</p>
  <p class="abs txt" style="left:40px;top:68px;width:62px;text-align:right;font-size:3.6px">Lorem ipsum dolor sit amet, consectetur adipiscing elit</p>
  <p class="abs txt" style="left:190px;top:68px;width:62px;font-size:3.6px">Lorem ipsum dolor sit amet, consectetur adipiscing elit</p>
  <p class="abs txt" style="left:40px;top:100px;width:62px;text-align:right;font-size:3.6px">Lorem ipsum dolor sit amet, consectetur adipiscing elit</p>
  <p class="abs txt" style="left:190px;top:100px;width:62px;font-size:3.6px">Lorem ipsum dolor sit amet, consectetur adipiscing elit</p>
  <p class="abs txt" style="left:104px;top:135px;width:80px;text-align:center;font-size:3.6px">Lorem ipsum dolor sit amet, consectetur adipiscing elit</p>
  <div class="rule"></div><span class="mark">Q</span><span class="client">client logo here</span>
</section>

<!-- Row 7 -->
<section class="slide c1 r7">
  <div class="photo" role="img" aria-label="Photo of doctors meeting with a patient" style="left:0;top:0;width:286px;height:90px;background:linear-gradient(120deg,#b7c2cc,#dde4ea 45%,#9aa8b4)"></div>
  <h2 class="title" style="color:#fff;top:13px">Content With Icon Sample</h2>
  <div class="abs" style="left:15px;top:78px;width:256px;display:grid;grid-template-columns:repeat(4,1fr);column-gap:8px;text-align:center">
    <div><svg width="26" height="26"><circle cx="13" cy="13" r="12" fill="var(--green)" stroke="#fff" stroke-width="1.5"/><circle cx="12" cy="12" r="4" fill="none" stroke="#fff" stroke-width="1.4"/><line x1="15" y1="15" x2="18.5" y2="18.5" stroke="#fff" stroke-width="1.6"/></svg><p style="font-size:4.5px;font-weight:600;color:var(--green)">Lorem Ipsum</p><p class="txt" style="font-size:3.4px">Lorem ipsum dolor sit amet, consectetur adipiscing elit</p></div>
    <div><svg width="26" height="26"><circle cx="13" cy="13" r="12" fill="var(--blue)" stroke="#fff" stroke-width="1.5"/><rect x="7.5" y="8" width="11" height="8" fill="none" stroke="#fff" stroke-width="1.2"/><line x1="13" y1="16" x2="13" y2="19" stroke="#fff" stroke-width="1.2"/></svg><p style="font-size:4.5px;font-weight:600;color:var(--blue)">Lorem Ipsum</p><p class="txt" style="font-size:3.4px">Lorem ipsum dolor sit amet, consectetur adipiscing elit</p></div>
    <div><svg width="26" height="26"><circle cx="13" cy="13" r="12" fill="var(--navy)" stroke="#fff" stroke-width="1.5"/><circle cx="13" cy="13" r="4.5" fill="none" stroke="#fff" stroke-width="2.2" stroke-dasharray="2 1.5"/><circle cx="13" cy="13" r="1.5" fill="#fff"/></svg><p style="font-size:4.5px;font-weight:600;color:var(--navy)">Lorem Ipsum</p><p class="txt" style="font-size:3.4px">Lorem ipsum dolor sit amet, consectetur adipiscing elit</p></div>
    <div><svg width="26" height="26"><circle cx="13" cy="13" r="12" fill="#fff" stroke="#9e9e9e" stroke-width="1.2"/><path d="M8 18 L17 9 M9 9 L18 18" stroke="#777" stroke-width="1.4"/></svg><p style="font-size:4.5px;font-weight:600;color:#777">Lorem Ipsum</p><p class="txt" style="font-size:3.4px">Lorem ipsum dolor sit amet, consectetur adipiscing elit</p></div>
  </div>
  <div class="rule"></div><span class="mark">Q</span><span class="copy">Copyright © 2016 Q Harbor Consulting. All rights reserved.</span><span class="client">client logo here</span>
</section>

<section class="slide c2 r7" style="background:#5b646c">
  <div class="photo" role="img" aria-label="Darkened photo of a doctor speaking with a patient" style="inset:0;background:linear-gradient(120deg,#7b858e,#4d565e 55%,#6a737b)"></div>
  <span class="pg" style="background:none">20</span>
  <h2 class="abs" style="left:0;right:0;top:13px;text-align:center;font-family:Ubuntu,sans-serif;font-weight:500;font-size:11px;color:#fff">Testimonials</h2>
  <svg class="abs" style="left:130px;top:51px" width="26" height="26"><circle cx="13" cy="13" r="11" fill="none" stroke="var(--green)" stroke-width="1.5"/><text x="13" y="18" font-size="13" font-weight="700" fill="var(--green)" text-anchor="middle" font-family="Open Sans,sans-serif">”</text></svg>
  <p class="abs" style="left:22px;right:22px;top:88px;text-align:center;font-size:4.4px;line-height:1.4;color:#fff">Lorem Ipsum is simply dummy text of the printing and typesetting industry. Lorem Ipsum has been the industry's standard dummy text ever since the 1500s, when an unknown printer took a galley of type and scrambled it to make a type specimen book.</p>
  <p class="abs" style="left:0;right:0;top:114px;text-align:center;font-size:5px;font-weight:700;font-style:italic;color:var(--green)">- John Doe -</p>
</section>

<section class="slide c3 r7">
  <svg class="abs" style="left:0;top:0" width="286" height="161">
    <rect x="0" y="0" width="286" height="10" fill="var(--navy)"/>
    <polygon points="0,10 130,10 145,22 286,22 286,14 150,14 135,2 0,2" fill="var(--blue)"/>
    <polygon points="0,141 60,141 70,148 286,148 286,161 0,161" fill="var(--green)"/>
    <polyline points="0,138 62,138 72,145 286,145" fill="none" stroke="var(--blue)" stroke-width="1.2"/>
  </svg>
  <h2 class="abs" style="left:9px;top:47px;font-family:Ubuntu,sans-serif;font-size:8.5px;font-weight:700;color:#222">THANK YOU FONT 24PT</h2>
  <div class="abs" style="left:9px;top:64px;font-size:3.6px;line-height:1.35;color:#555">
    <p style="font-weight:700;color:#222;font-style:italic">ADDRESS</p><p>Lorem ipsum</p>
    <p style="font-weight:700;color:#222;font-style:italic;margin-top:1px">PHONE/FAX</p><p>Call 4321-300-0000<br>Lo-Call Number: 4321-300-3000</p>
    <p style="font-weight:700;color:#222;font-style:italic;margin-top:1px">EMAIL</p><p>loremipsum@example.com</p>
    <p style="font-weight:700;color:#222;font-style:italic;margin-top:1px">WEBSITE</p><p>www.example.com</p>
  </div>
  <p class="abs logo-name" style="left:206px;top:58px;font-size:7px;text-align:center;width:70px;line-height:1.1">Q Harbor<br><span style="font-size:3.5px;letter-spacing:1px">CONSULTING</span></p>
  <p class="abs" style="left:180px;top:88px;width:100px;font-size:3.6px;line-height:1.35;color:#444">Lorem Ipsum is simply dummy text of the printing and typesetting industry. Lorem Ipsum has been the industry's standard dummy text ever since the 1500s, when an unknown printer took a galley of type and scrambled it. The industry's standard dummy text ever since the 1500s, when an unknown printer took a galley.</p>
</section>

</body>
</html>
```